Harborline Capital Inc. Investor Presentation

We would like a PowerPoint presentation to attract prospective investors. It needs to look extremely professional since we are a financial lending institution, and seeking capital investors. We specialize in Private Lending with Mortgage Backed Securities, both Residential and Commercial properties.

```html
<!DOCTYPE html>
<html lang="en">
<head>
<meta charset="utf-8">
<title>Harborline Capital Inc. — Investor Presentation</title>
<link href="https://fonts.googleapis.com/css2?family=Signika:wght@400;600&family=Didact+Gothic&display=swap" rel="stylesheet">
<style>
:root{
  --ink:#3b3b3b;
  --blue:#0d5697;
  --blue-light:#3d86c6;
  --gray:#cdcdcd;
  --rule:#d6d6d6;
  --paper:#ffffff;
  --stage:#0b0b0b;
  --muted:#6a6a6a;
}
*{margin:0;padding:0;box-sizing:border-box}
html,body{width:1200px;height:714px;overflow:hidden;background:var(--stage)}
body{position:relative;font-family:"Didact Gothic",sans-serif;color:var(--ink)}
.slide{position:absolute;width:378px;height:212px;background:var(--paper);overflow:hidden}
.abs{position:absolute}
.head{font-family:"Signika",sans-serif;font-weight:600;color:var(--ink);line-height:1.12}
.accent{color:var(--blue)}
.small{font-size:5.6px;line-height:8.7px;color:var(--muted)}
.photo{position:absolute}
.photo-office{background:linear-gradient(135deg,#e7e1d8,#c8b8a3 45%,#7d6a5a 70%,#d9d4cc)}
.photo-tower{background:linear-gradient(160deg,#9cc4ee 0%,#5d96d6 35%,#1d5ea8 60%,#0f3b72 100%)}
.photo-desk{background:linear-gradient(135deg,#f1ede8,#c7a27e 45%,#9b7656 70%,#ece7e2)}

/* slide 1 cover */
.cover{background:linear-gradient(120deg,#ecedef,#e2e4e7 60%,#e9eaec)}
.cover .band{left:288px;top:0;width:60px;height:212px;background:var(--blue-light)}
.cover .edge{left:348px;top:0;width:30px;height:212px;background:#e1e1e1}
.cover h1{left:37px;top:123px;font-size:19.5px;color:var(--blue)}
.cover p{left:38px;top:147px;width:220px;font-size:9.4px;line-height:13.5px;color:#444}

/* slide 2 */
.title-band{left:0;top:157px;width:378px;height:55px;background:var(--blue)}
.title-band h2{left:29px;top:16px;font-size:21px;color:#fff}
.title-band p{left:219px;top:12px;font-size:7.1px;line-height:8.3px;color:#fff}

/* progress bars */
.meter{left:28px;width:144px}
.meter .label{display:flex;justify-content:space-between;font-size:6.2px;color:#555}
.meter .track{margin-top:4px;height:2px;background:var(--rule)}
.meter .fill{height:2px;background:var(--blue)}

/* rings */
.ring{position:absolute;top:84px;width:38px;height:38px}
.ring-label{position:absolute;top:132px;width:60px;text-align:center;font-family:"Signika",sans-serif;font-size:6.8px;font-weight:600;color:#444}
.link{position:absolute;top:102px;width:22px;height:1.2px;background:#444}

.legend{right:32px;text-align:right}
.legend h4{font-size:6.4px;font-weight:400;color:#444;letter-spacing:.2px}
.legend .sw{position:absolute;right:-13px;top:1px;width:6px;height:6px}
</style>
</head>
<body>

<!-- Cover -->
<section class="slide cover" style="left:16px;top:17px">
  <div class="photo" role="img" aria-label="Faded photo of a hand pointing at analytics on a laptop screen" style="inset:0;background:linear-gradient(120deg,#e9eaed,#dcdfe3 40%,#eeeeef);opacity:.9"></div>
  <div class="abs band"></div>
  <div class="abs edge"></div>
  <h1 class="abs head">Harborline Capital Inc.</h1>
  <p class="abs">Lorem ipsum dolor sit amet, consec- tetur adipiscing elit. Vivamus eget vestibulumex, ut tincidunt nisl.</p>
</section>

<!-- Project title -->
<section class="slide" style="left:407px;top:19px">
  <div class="photo photo-tower" role="img" aria-label="Glass office tower seen from below against blue sky" style="left:0;top:0;width:378px;height:154px"></div>
  <div class="abs" style="left:0;top:154px;width:378px;height:3px;background:#7b7f86"></div>
  <div class="abs title-band">
    <h2 class="abs head">Project Title here</h2>
    <p class="abs">Lorem ipsum dolor sit amet, consectetur<br>adipiscing elit vivamus eget.<br>Lorem ipsum dolor sit amet, consectetur<br>adipiscing elit vivamus eget.</p>
  </div>
</section>

<!-- Progress slide -->
<section class="slide" style="left:806px;top:20px">
  <h2 class="abs head" style="left:27px;top:49px;font-size:16.5px;font-weight:400">Imperdiet arcu</h2>
  <div class="abs" style="left:28px;top:85px;width:33px;height:1.4px;background:#333"></div>
  <div class="abs meter" style="top:113px"><div class="label"><span>Lorem Ipsum</span><span>65%</span></div><div class="track"><div class="fill" style="width:65%"></div></div></div>
  <div class="abs meter" style="top:139px"><div class="label"><span>Dolor Sit</span><span>88%</span></div><div class="track"><div class="fill" style="width:83%"></div></div></div>
  <div class="abs meter" style="top:164px"><div class="label"><span>Commodo Lectus</span><span>42%</span></div><div class="track"><div class="fill" style="width:39%"></div></div></div>
  <div class="abs" style="left:221px;top:66px;width:34px;height:81px;background:var(--gray)"></div>
  <div class="photo photo-tower" role="img" aria-label="Glass office tower against blue sky" style="left:255px;top:25px;width:123px;height:163px"></div>
  <div class="abs" style="left:354px;top:0;width:24px;height:25px;background:var(--blue)"></div>
  <div class="abs" style="left:354px;top:188px;width:24px;height:24px;background:var(--blue)"></div>
</section>

<!-- Thank you -->
<section class="slide" style="left:18px;top:255px">
  <div class="abs" style="left:0;top:0;width:14px;height:79px;background:var(--gray)"></div>
  <div class="abs" style="left:0;top:95px;width:14px;height:14px;background:var(--blue)"></div>
  <div class="abs" style="left:341px;top:19px;width:37px;height:7px;background:var(--blue)"></div>
  <h2 class="abs head" style="left:0;width:378px;top:70px;text-align:center;font-size:30px;font-weight:600;letter-spacing:.5px">THANK <span class="accent">YOU</span></h2>
  <p class="abs" style="left:0;width:378px;top:114px;text-align:center;font-size:7.2px;line-height:8.4px;color:#555">Lorem ipsum dolor sit amet, consectetur<br>adipiscing elit vivamus eget.</p>
  <p class="abs" style="left:0;width:378px;top:136px;text-align:center;font-size:6.3px;color:var(--blue)">www.harborlinecapital.com</p>
  <div class="abs" style="left:0;top:195px;width:200px;height:1.6px;background:#444"></div>
</section>

<!-- Rings -->
<section class="slide" style="left:407px;top:255px">
  <div class="abs" style="left:274px;top:0;width:104px;height:7px;background:var(--gray)"></div>
  <div class="abs" style="left:0;top:200px;width:13px;height:12px;background:var(--blue)"></div>
  <h2 class="abs head" style="left:27px;top:21px;font-size:14.5px;font-weight:400">Arcu <span class="accent" style="font-weight:600">congue</span></h2>
  <svg class="ring" style="left:62px" viewBox="0 0 38 38"><circle cx="19" cy="19" r="16.5" fill="none" stroke="var(--rule)" stroke-width="3"/><circle cx="19" cy="19" r="16.5" fill="none" stroke="var(--blue)" stroke-width="3" stroke-dasharray="77.8 103.7" transform="rotate(-90 19 19)"/><text x="19" y="22" text-anchor="middle" font-family="Signika,sans-serif" font-weight="600" font-size="8.5" fill="#3b3b3b">75%</text></svg>
  <svg class="ring" style="left:134px" viewBox="0 0 38 38"><circle cx="19" cy="19" r="16.5" fill="none" stroke="var(--rule)" stroke-width="3"/><circle cx="19" cy="19" r="16.5" fill="none" stroke="var(--blue)" stroke-width="3" stroke-dasharray="48.7 103.7" transform="rotate(-90 19 19)"/><text x="19" y="22" text-anchor="middle" font-family="Signika,sans-serif" font-weight="600" font-size="8.5" fill="#3b3b3b">47%</text></svg>
  <svg class="ring" style="left:206px" viewBox="0 0 38 38"><circle cx="19" cy="19" r="16.5" fill="none" stroke="var(--rule)" stroke-width="3"/><circle cx="19" cy="19" r="16.5" fill="none" stroke="var(--blue)" stroke-width="3" stroke-dasharray="86.1 103.7" transform="rotate(-90 19 19)"/><text x="19" y="22" text-anchor="middle" font-family="Signika,sans-serif" font-weight="600" font-size="8.5" fill="#3b3b3b">83%</text></svg>
  <svg class="ring" style="left:278px" viewBox="0 0 38 38"><circle cx="19" cy="19" r="16.5" fill="none" stroke="var(--rule)" stroke-width="3"/><circle cx="19" cy="19" r="16.5" fill="none" stroke="var(--blue)" stroke-width="3" stroke-dasharray="67.4 103.7" transform="rotate(-90 19 19)"/><text x="19" y="22" text-anchor="middle" font-family="Signika,sans-serif" font-weight="600" font-size="8.5" fill="#3b3b3b">65%</text></svg>
  <div class="link" style="left:106px"></div>
  <div class="link" style="left:178px"></div>
  <div class="link" style="left:250px"></div>
  <div class="ring-label" style="left:51px">Lorem Ipsum</div>
  <div class="ring-label" style="left:123px">Lorem Ipsum</div>
  <div class="ring-label" style="left:195px">Lorem Ipsum</div>
  <div class="ring-label" style="left:267px">Lorem Ipsum</div>
</section>

<!-- Line chart -->
<section class="slide" style="left:806px;top:255px">
  <svg class="abs" style="left:0;top:0" width="378" height="212" viewBox="0 0 378 212" font-family="Didact Gothic,sans-serif">
    <g stroke="#cfcfcf" stroke-width=".8">
      <line x1="54" y1="64.5" x2="204" y2="64.5"/><line x1="54" y1="79.4" x2="204" y2="79.4"/><line x1="54" y1="94.4" x2="204" y2="94.4"/><line x1="54" y1="108.8" x2="204" y2="108.8"/><line x1="54" y1="123.7" x2="204" y2="123.7"/><line x1="54" y1="138.2" x2="204" y2="138.2"/>
    </g>
    <line x1="54" y1="49" x2="54" y2="153" stroke="#bbb" stroke-width="1"/>
    <line x1="54" y1="153" x2="204" y2="153" stroke="#bbb" stroke-width="1"/>
    <g font-size="6.6" fill="#888" text-anchor="end"><text x="46" y="59">100%</text><text x="46" y="104">50%</text><text x="46" y="148">0%</text></g>
    <g font-size="6.6" fill="#999" text-anchor="middle"><text x="64" y="165">JAN</text><text x="108" y="165">MAR</text><text x="151" y="165">MAY</text><text x="195" y="165">JUL</text></g>
    <polyline fill="none" stroke="#3b3b3b" stroke-width="1.1" points="54,116 75.1,98.2 96.3,116 118,103 139.6,131 160.8,67.4 182,58.7 202.2,74.6"/>
    <polyline fill="none" stroke="var(--blue)" stroke-width="1.1" points="54,131.4 75.1,108.3 96.3,102.1 118,79.4 139.6,93.9 160.8,86.2 182,105 202.2,102.1"/>
    <g fill="#3b3b3b"><circle cx="75.1" cy="98.2" r="2"/><circle cx="96.3" cy="116" r="2"/><circle cx="118" cy="103" r="2"/><circle cx="139.6" cy="131" r="2"/><circle cx="160.8" cy="67.4" r="2"/><circle cx="182" cy="58.7" r="2"/><circle cx="202.2" cy="74.6" r="2"/></g>
    <g fill="var(--blue)"><circle cx="75.1" cy="108.3" r="2"/><circle cx="96.3" cy="102.1" r="2"/><circle cx="118" cy="79.4" r="2"/><circle cx="139.6" cy="93.9" r="2"/><circle cx="160.8" cy="86.2" r="2"/><circle cx="182" cy="105" r="2"/><circle cx="202.2" cy="102.1" r="2"/></g>
  </svg>
  <div class="abs" style="left:247px;top:34px;width:22px;height:1.2px;background:#333"></div>
  <h2 class="abs head" style="right:31px;top:27px;text-align:right;font-size:13.5px"><span class="accent">Fermentum</span><br>Sapien</h2>
  <div class="abs legend" style="top:99px"><h4>LOREM IPSUM</h4><span class="sw" style="background:var(--blue)"></span><p class="small" style="margin-top:3px">Lorem ipsum dolor sit amet,<br>consectetur adipiscing.</p></div>
  <div class="abs legend" style="top:149px"><h4>LOREM IPSUM</h4><span class="sw" style="background:#3b3b3b"></span><p class="small" style="margin-top:3px">Lorem ipsum dolor sit amet,<br>consectetur adipiscing.</p></div>
  <div class="abs" style="left:369px;top:90px;width:9px;height:122px;background:var(--gray)"></div>
</section>

<!-- Photo strip -->
<section class="slide" style="left:19px;top:481px">
  <h2 class="abs head" style="right:28px;top:23px;font-size:13.5px">Pellentesque a <span class="accent">liberor</span></h2>
  <div class="abs" style="left:356px;top:23px;width:1.3px;height:17px;background:#333"></div>
  <div class="photo photo-desk" role="img" aria-label="Business people reviewing financial charts with a pen at a laptop" style="left:0;top:62px;width:182px;height:92px"></div>
  <div class="abs" style="left:194px;top:62px;width:72px;height:92px;background:var(--blue)"></div>
  <p class="abs" style="left:216px;top:84px;font-size:10.5px;line-height:17px;color:#fff">Lorem<br>ipsum<br>dolor</p>
  <div class="photo photo-desk" role="img" aria-label="Hand holding a pen over a printed chart report" style="left:279px;top:62px;width:99px;height:92px"></div>
  <p class="abs small" style="left:23px;top:176px">Lorem ipsum dolor sit amet, consectetur<br>adipiscing elit. Vivamus eget vestib</p>
</section>

<!-- Collage -->
<section class="slide" style="left:408px;top:481px">
  <div class="abs" style="left:0;top:0;width:18px;height:18px;background:var(--gray)"></div>
  <h2 class="abs head" style="left:27px;top:52px;font-size:13.5px;line-height:16px"><span class="accent">Dignissim</span> vitae<br>mauris eget,<br>vehicula</h2>
  <div class="abs" style="left:27px;top:117px;width:43px;height:1.6px;background:var(--blue)"></div>
  <p class="abs small" style="left:27px;top:134px">Lorem ipsum dolor sit amet, consectetur<br>adipiscing elit. Vivamus eget vestibulum<br>ex, ut tincidunt nisl. Nunc tortor libero,,</p>
  <div class="abs" style="left:144px;top:164px;width:49px;height:19px;background:var(--blue)"></div>
  <div class="photo photo-desk" role="img" aria-label="Hands gesturing over a printed financial chart" style="left:169px;top:39px;width:65px;height:134px"></div>
  <div class="photo photo-desk" role="img" aria-label="Hand with a pen reviewing a bar chart report beside a laptop" style="left:244px;top:4px;width:118px;height:208px"></div>
</section>

<!-- Closing statement -->
<section class="slide" style="left:806px;top:483px">
  <div class="abs" style="left:0;top:61px;width:26px;height:41px;background:var(--blue)"></div>
  <div class="photo photo-desk" role="img" aria-label="Two people reviewing and signing a document at a desk" style="left:26px;top:29px;width:163px;height:104px"></div>
  <h2 class="abs head" style="right:28px;top:94px;text-align:right;font-size:13px;line-height:16.5px;font-weight:400">Lorem ipsum dolor sit<br>amet, <span class="accent" style="font-weight:600">consectetur</span></h2>
  <div class="abs" style="left:313px;top:131px;width:34px;height:1.4px;background:#333"></div>
  <p class="abs small" style="left:29px;top:157px">Lorem ipsum dolor sit amet, consec-<br>tetur adipiscing elit. Vivamus eget<br>vestibulumex, ut tincidunt.</p>
  <div class="abs" style="left:214px;top:205px;width:164px;height:7px;background:var(--gray)"></div>
</section>

</body>
</html>
```